Website design in Wordpress for Golf Simulator Center

We are opening a new golf simulator center in Copenhagen, and need a website design. We are using wordpress, and our site is https://fernway-putt.dk
We will need a design for the frontpage, and a design for subpages (which we will be reusing for all subpages).
Logo is as seen on the site, and our base color scheme is leaf green.
As text, take the text on the current website, or put some placeholder text in english.
Should be responsive and look good on both desktop and mobile.
Target Market(s)
Male, 18-60, golf players
Coding
Coded - Design and coding required
Number of Pages Required
2 page
Font styles to use
Look and feel

```html
<!DOCTYPE html>
<html lang="en">
<head>
<meta charset="utf-8">
<title>Fernway Putt – Golf Simulator in Valby</title>
<link rel="stylesheet" href="https://fonts.googleapis.com/css2?family=Oswald:wght@400;500;600&family=Roboto:wght@400;500&display=swap">
<style>
:root{
  --green:#0a7a0a;
  --green-dark:#075e07;
  --ink:#1e1e1e;
  --text:#444;
  --muted:#888;
  --mist:#dfe8de;
  --footer:#0b0b0b;
  --white:#fff;
}
*{box-sizing:border-box;margin:0;padding:0}
html,body{width:1200px;height:4134px;overflow:hidden}
body{font-family:"Roboto",Arial,sans-serif;color:var(--text);background:var(--white);position:relative}
section,header,footer{position:absolute;left:0;width:1200px}
.abs{position:absolute}
.btn{position:absolute;display:flex;align-items:center;justify-content:center;font-family:"Oswald",sans-serif;font-weight:500;font-size:15px;color:var(--white);background:var(--green);text-transform:uppercase;letter-spacing:.2px;clip-path:polygon(0 8%,100% 0,100% 92%,0 100%);text-decoration:none}
.btn.light{background:var(--white);color:var(--green)}
.h2{font-family:"Oswald",sans-serif;font-weight:500;font-size:32px;color:var(--ink);text-transform:uppercase;line-height:46px;display:flex;align-items:center;gap:14px}
.h2 em{font-style:normal;color:var(--green)}
.mark{width:30px;height:30px;border:4px solid var(--green);display:inline-block}
.center{justify-content:center;left:0;width:1200px}

/* header */
.site-header{top:0;height:84px;background:var(--white)}
.brand{display:flex;align-items:center;gap:8px;font-family:"Oswald",sans-serif;font-weight:600;font-size:30px;color:var(--green);text-transform:uppercase}
.brand .sq{width:22px;height:22px;background:var(--green)}
.nav a{position:absolute;top:30px;font-size:15px;color:#555;text-decoration:none}
.nav a.active{color:var(--green);border-bottom:1px solid var(--green)}

/* hero */
.hero{top:84px;height:472px;background:linear-gradient(180deg,#3f4c66 0%,#b8846a 30%,#8a5a40 50%,#3b3b44 68%,#2a3a55 100%)}
.hero h1{position:absolute;top:108px;left:0;width:1200px;text-align:center;font-family:"Oswald",sans-serif;font-weight:500;font-size:52px;color:var(--white);text-transform:uppercase}
.hero p{position:absolute;top:186px;left:280px;width:640px;text-align:center;font-size:15px;line-height:26px;color:var(--white)}
.dots{position:absolute;top:429px;left:573px;display:flex;gap:5px}
.dots i{width:14px;height:14px;border-radius:50%;background:var(--white);display:block}
.dots i.on{background:var(--green);border:2px solid var(--white)}

/* about */
.about{top:556px;height:570px}
.about .photo{left:157px;top:86px;width:345px;height:361px;background:linear-gradient(135deg,#dfe6ee,#6c8f5e 55%,#3b5d2f);clip-path:polygon(0 0,100% 15%,100% 88%,0 100%)}
.about .copy p{font-size:14.5px;line-height:25.7px;color:#444;margin-bottom:12px}

/* green band */
.band{top:1126px;height:472px;background:var(--green)}
.band .photo{left:690px;top:0;width:510px;height:472px;background:linear-gradient(180deg,#4d4a3a 0%,#a98a4e 25%,#5f7a2c 45%,#3c6a1c 100%)}
.band .fade{left:560px;top:0;width:260px;height:472px;background:linear-gradient(90deg,var(--green),rgba(10,122,10,0))}
.band p{font-size:15px;line-height:25.7px;color:var(--white);text-align:justify}

/* membership */
.member{top:1598px;height:747px}
.member .card{left:322px;top:152px;width:554px;height:308px;background:var(--white);box-shadow:0 2px 10px rgba(0,0,0,.25);padding:10px}
.member .card div{width:100%;height:100%;background:linear-gradient(135deg,#173016,#2c6b22 45%,#1a3a1a)}
.member p{position:absolute;left:141px;top:493px;width:918px;text-align:center;font-size:13px;line-height:23px;color:#444}

/* blog */
.blog{top:2345px;height:857px;background:var(--mist)}
.post{position:absolute;background:var(--white);box-shadow:0 1px 6px rgba(0,0,0,.1)}
.post .img{position:absolute;left:12px;top:12px}
.post h3{position:absolute;font-family:"Oswald",sans-serif;font-weight:400;font-size:20px;line-height:28px;color:var(--ink)}
.post h3.g{color:var(--green);font-size:18px}
.post .date{position:absolute;font-size:15px;color:var(--muted);display:flex;align-items:center;gap:6px}
.post .more{position:absolute;font-family:"Oswald",sans-serif;font-weight:500;font-size:15px;color:var(--green);display:flex;align-items:center;gap:6px}

/* contact */
.contact{top:3202px;height:573px}
.field{position:absolute;background:var(--white);box-shadow:0 1px 8px rgba(0,0,0,.12);font-size:15px;color:#888;padding:28px 26px}

/* footer */
.site-footer{top:3775px;height:359px;background:var(--footer);color:#ddd}
.site-footer h4{position:absolute;top:70px;font-family:"Oswald",sans-serif;font-weight:500;font-size:19px;color:var(--white)}
.site-footer ul{position:absolute;top:110px;list-style:none;font-size:15px;line-height:25.7px}
.site-footer li::before{content:"»";margin-right:12px}
.site-footer .info{position:absolute;left:863px;top:110px;font-size:15px;line-height:25.7px}
.social{position:absolute;width:38px;height:38px;border-radius:50%;background:var(--white)}
.social.g{background:var(--green)}
.copy-line{position:absolute;top:4074px;left:0;width:1200px;text-align:center;font-size:14px;color:#ddd}
</style>
</head>
<body>

<header class="site-header">
  <div class="brand abs" style="left:109px;top:24px"><span>Fernway Putt</span><span class="sq"></span></div>
  <nav class="nav">
    <a class="active" style="left:433px">Home</a>
    <a style="left:521px">Blog</a>
    <a style="left:597px">Find your way</a>
    <a style="left:736px">Dictionary</a>
    <a style="left:852px">Contact us</a>
  </nav>
  <svg class="abs" style="left:960px;top:33px" width="16" height="16" viewBox="0 0 16 16"><circle cx="6.5" cy="6.5" r="4.5" fill="none" stroke="#333" stroke-width="2"/><path d="M10 10l4 4" stroke="#333" stroke-width="2.4"/></svg>
  <svg class="abs" style="left:1003px;top:27px" width="28" height="28" viewBox="0 0 28 28"><circle cx="14" cy="14" r="14" fill="var(--green)"/><circle cx="14" cy="14" r="7" fill="none" stroke="#fff" stroke-width="1.5"/><path d="M7 14h14M14 7c-4 4-4 10 0 14M14 7c4 4 4 10 0 14" stroke="#fff" stroke-width="1.3" fill="none"/></svg>
  <span class="abs" style="left:1040px;top:31px;font-family:Oswald,sans-serif;font-size:15px;color:#333">ENG</span>
  <svg class="abs" style="left:1070px;top:36px" width="12" height="8" viewBox="0 0 12 8"><path d="M1 1l5 5 5-5" stroke="#999" stroke-width="2" fill="none"/></svg>
</header>

<section class="hero">
  <div class="abs" style="inset:0" role="img" aria-label="Copenhagen waterfront with historic buildings at sunset"></div>
  <h1>Golf Simulator in Valby</h1>
  <p>Indoor golf center with 8 simulators in Valby. Play golf indoors in all weathers, whether driving range or a full 18-hole round.</p>
  <a class="btn" style="left:537px;top:266px;width:124px;height:50px">Get started</a>
  <div class="dots"><i></i><i class="on"></i><i></i></div>
</section>

<section class="about">
  <svg class="abs" style="left:112px;top:303px" width="96" height="186" viewBox="0 0 96 186">
    <g fill="var(--green)">
      <circle cx="3" cy="3" r="1.6"/><circle cx="25" cy="3" r="1.6"/>
      <circle cx="3" cy="25" r="1.6"/><circle cx="25" cy="25" r="1.6"/>
      <circle cx="3" cy="47" r="1.6"/><circle cx="25" cy="47" r="1.6"/>
      <circle cx="3" cy="69" r="1.6"/><circle cx="25" cy="69" r="1.6"/>
      <circle cx="3" cy="91" r="1.6"/><circle cx="25" cy="91" r="1.6"/>
      <circle cx="3" cy="113" r="1.6"/><circle cx="25" cy="113" r="1.6"/>
      <circle cx="3" cy="135" r="1.6"/><circle cx="25" cy="135" r="1.6"/><circle cx="47" cy="135" r="1.6"/><circle cx="69" cy="135" r="1.6"/><circle cx="91" cy="135" r="1.6"/>
      <circle cx="3" cy="157" r="1.6"/><circle cx="25" cy="157" r="1.6"/><circle cx="47" cy="157" r="1.6"/><circle cx="69" cy="157" r="1.6"/><circle cx="91" cy="157" r="1.6"/>
      <circle cx="3" cy="179" r="1.6"/><circle cx="25" cy="179" r="1.6"/><circle cx="47" cy="179" r="1.6"/><circle cx="69" cy="179" r="1.6"/><circle cx="91" cy="179" r="1.6"/>
    </g>
  </svg>
  <div class="photo abs" role="img" aria-label="Golfer silhouette in front of a simulator screen showing a fairway"></div>
  <div class="copy abs" style="left:597px;top:80px;width:490px">
    <div class="h2" style="font-size:31px;line-height:45px;display:block">Golf <em>Simulator</em> in Valby<br><em>Opens</em> January 2023 <span class="mark" style="vertical-align:-4px;margin-left:8px"></span></div>
    <div style="margin-top:20px">
      <p>In January 2023, a new golf simulator center will open in Valby with 8 simulators of the Skyline 4 type. We look forward to being able to welcome new and experienced golfers. With us, you can practice all kinds of shots indoors, sheltered from rain and snow, or play an entire 18-hole course in half the time.</p>
      <p>Each simulator gives you a precise radar measurement of your stroke, so you can practice exactly as you want on a virtual driving range, or on one of our many virtual courses from around the world.</p>
    </div>
  </div>
  <a class="btn" style="left:598px;top:430px;width:122px;height:54px">Learn more</a>
</section>

<section class="band">
  <div class="photo abs" role="img" aria-label="Golfer lining up a putt in a simulator bay"></div>
  <div class="fade abs"></div>
  <div class="h2 abs" style="left:111px;top:56px;color:#fff">New Golf Simulator <span class="mark" style="border-color:#fff"></span></div>
  <p class="abs" style="left:111px;top:136px;width:478px">Lorem ipsum dolor sit amet, consectetur adipiscing elit, sed do eiusmod tempor incididunt ut labore et dolore magna aliqua. Ut enim ad minim veniam, quis nostrud exercitation ullamco laboris nisi ut aliquip ex ea commodo consequat. Duis aute irure dolor in reprehenderit in voluptate velit esse cillum dolore eu fugiat nulla pariatur. Excepteur sint occaecat cupidatat non proident, sunt in culpa qui officia deserunt mollit anim id est laborum.</p>
  <a class="btn light" style="left:111px;top:359px;width:123px;height:52px">Learn more</a>
</section>

<section class="member">
  <div class="h2 center abs" style="top:76px;display:flex">Buy a <em>Starter</em> Membership <span class="mark"></span></div>
  <div class="card abs"><div role="img" aria-label="Starter membership poster with price and included benefits"></div></div>
  <p>Are you missing the perfect gift for the person who has everything? Then we have the solution! Give a membership to Fernway Putt as a gift! When we open in January, we will be selling a special start-up membership, which is the same one you can buy right now for a gift or for yourself. For DKK 500, you will be sent a voucher by email, which you can print. The voucher can be redeemed with us for a start-up membership. It can be redeemed when we open and until 31/8-2023. We will open no later than 1/2-2023</p>
  <a class="btn" style="left:492px;top:609px;width:217px;height:50px">Order starter membership</a>
</section>

<section class="blog">
  <div class="h2 center abs" style="top:80px">Latest <em>Blog</em> <span class="mark"></span></div>

  <article class="post" style="left:111px;top:170px;width:489px;height:497px">
    <div class="img" style="width:465px;height:318px;background:linear-gradient(135deg,#1f3a22,#3f7a38 60%,#9fc48a)" role="img" aria-label="Golfer swinging in a simulator bay"></div>
    <h3 style="left:12px;top:352px">The first blow has been struck!</h3>
    <div class="date" style="left:12px;top:393px"><svg width="14" height="14" viewBox="0 0 14 14"><rect x="1" y="2" width="12" height="11" fill="none" stroke="#aaa" stroke-width="1.5"/><path d="M1 5h12" stroke="#aaa" stroke-width="1.5"/></svg>2022-12-22</div>
    <div class="more" style="left:12px;top:448px">READ MORE <svg width="16" height="10" viewBox="0 0 16 10"><path d="M0 5h14M10 1l4 4-4 4" stroke="var(--green)" stroke-width="1.6" fill="none"/></svg></div>
  </article>

  <article class="post" style="left:635px;top:170px;width:453px;height:239px">
    <div class="img" style="left:10px;top:10px;width:191px;height:219px;background:linear-gradient(180deg,#c88a4a,#5a6f86 45%,#2f5a2a)" role="img" aria-label="Simulator target mat with city skyline screen"></div>
    <h3 class="g" style="left:230px;top:38px">Golf training on a<br>simulator</h3>
    <div class="date" style="left:230px;top:111px"><svg width="14" height="14" viewBox="0 0 14 14"><rect x="1" y="2" width="12" height="11" fill="none" stroke="#aaa" stroke-width="1.5"/><path d="M1 5h12" stroke="#aaa" stroke-width="1.5"/></svg>2022-08-04</div>
    <div class="more" style="left:230px;top:181px">READ MORE <svg width="16" height="10" viewBox="0 0 16 10"><path d="M0 5h14M10 1l4 4-4 4" stroke="var(--green)" stroke-width="1.6" fill="none"/></svg></div>
  </article>

  <article class="post" style="left:635px;top:428px;width:453px;height:239px">
    <div class="img" style="left:10px;top:10px;width:191px;height:219px;background:linear-gradient(135deg,#b9b4a8,#6d6a63 50%,#3a3836)" role="img" aria-label="Golf clubs in a bag"></div>
    <h3 style="left:230px;top:38px;font-size:18px">Golf equipment for use on<br>a simulator</h3>
    <div class="date" style="left:230px;top:111px"><svg width="14" height="14" viewBox="0 0 14 14"><rect x="1" y="2" width="12" height="11" fill="none" stroke="#aaa" stroke-width="1.5"/><path d="M1 5h12" stroke="#aaa" stroke-width="1.5"/></svg>2022-07-20</div>
    <div class="more" style="left:230px;top:181px">READ MORE <svg width="16" height="10" viewBox="0 0 16 10"><path d="M0 5h14M10 1l4 4-4 4" stroke="var(--green)" stroke-width="1.6" fill="none"/></svg></div>
  </article>

  <a class="btn" style="left:539px;top:720px;width:122px;height:52px">Learn more</a>
</section>

<section class="contact">
  <div class="h2 center abs" style="top:84px">Contact <em>Us</em> <span class="mark"></span></div>
  <div class="field" style="left:202px;top:175px;width:254px;height:67px;padding-top:24px">Name</div>
  <div class="field" style="left:473px;top:175px;width:254px;height:67px;padding-top:24px">Phone</div>
  <div class="field" style="left:744px;top:175px;width:254px;height:67px;padding-top:24px">Email</div>
  <div class="field" style="left:202px;top:266px;width:796px;height:128px;padding-top:24px">Message</div>
  <a class="btn" style="left:539px;top:433px;width:122px;height:51px">Submit</a>
</section>

<footer class="site-footer">
  <div class="brand abs" style="left:111px;top:88px;font-size:32px"><span>Fernway Putt</span><span class="sq"></span></div>
  <div class="social g" style="left:109px;top:170px" aria-label="Social profile"></div>
  <div class="social" style="left:154px;top:170px" aria-label="Social profile"></div>
  <div class="social" style="left:196px;top:170px" aria-label="Social profile"></div>
  <div class="social" style="left:239px;top:170px" aria-label="Social profile"></div>
  <div class="abs" style="left:390px;top:67px;width:1px;height:176px;background:#333"></div>

  <h4 style="left:432px">Quick Links</h4>
  <ul style="left:432px"><li>Home</li><li>Blog</li><li>Find your way</li><li>Dictionary</li><li>Contact us</li></ul>

  <h4 style="left:638px">Our Company</h4>
  <ul style="left:638px"><li>Terms &amp; Conditions</li><li>Privacy Policy</li><li>About Us</li><li>Support</li></ul>

  <h4 style="left:863px">Contact us</h4>
  <div class="info">
    <div style="display:flex;gap:10px"><svg width="13" height="18" viewBox="0 0 13 18" style="margin-top:4px"><path d="M6.5 0C2.9 0 0 2.8 0 6.3 0 11 6.5 18 6.5 18S13 11 13 6.3C13 2.8 10.1 0 6.5 0z" fill="#fff"/><circle cx="6.5" cy="6.3" r="2.4" fill="var(--footer)"/></svg><div>2500 Valby<br>CVR: 40917362</div></div>
    <div style="display:flex;gap:10px;margin-top:14px;align-items:center"><svg width="15" height="15" viewBox="0 0 15 15"><path d="M3 0l3 3.5-2 2c1 2 3 4 5 5l2-2L15 12l-2.5 3C6 14 1 9 0 2.5z" fill="#fff"/></svg>71 42 55 08</div>
    <div style="display:flex;gap:10px;margin-top:24px;align-items:center"><svg width="16" height="12" viewBox="0 0 16 12"><rect width="16" height="12" fill="#fff"/><path d="M0 0l8 6 8-6" stroke="var(--footer)" stroke-width="1.4" fill="none"/></svg>info@fernway-putt.com</div>
  </div>
</footer>
<div class="copy-line">©Copyrights 2023 Fernway-putt &nbsp; | &nbsp; All Rights Reserved</div>

</body>
</html>
```